Veterinary Entrepreneurship Podcast Needs Image Design

I need some images designed for a new podcast called "Veterinary Entrepreneurship: The Dorian Kelboe Journals".

I need a cover image for Quilly Casts: "Artwork must be in the JPEG or PNG file formats and in the RGB color space with a minimum size of 1400 x 1400 pixels and a maximum size of 3000 x 3000 pixels at 72 DPI."

The podcasts is essentially about me charting daily my journey as an entrepreneur. Looking for a design which is stylish but fun, communicates innovation, dynamism etc. To include the attached head shot photo and one version of the attached signatures.

Target Market(s)

Veterinary

Industry/Entity Type

Veterinary

Font styles to use
Sans Serif

Colors

Designer to choose colors to be used in the design.

Requirements
Must have
• The name of the podcast, my head shot photo and one of the signature files I uploaded.
Nice to have
• Nothing particularly comes to mind
Should not have
• No photos of animals please although happy to see illustrations, outlines etc.

```html
<!DOCTYPE html>
<html lang="en">
<head>
<meta charset="utf-8">
<title>Veterinary Entrepreneurship: The Dorian Kelboe Journals</title>
<link href="https://fonts.googleapis.com/css2?family=Amatic+SC:wght@400;700&display=swap" rel="stylesheet">
<style>
  :root {
    --sun-yellow: #fdd800;
    --paw-yellow: #fde766;
    --brick-red: #c1290f;
    --portrait-tone: #b98a6e;
    --portrait-dark: #3a3330;
    --ink: #111111;
  }
  html, body {
    margin: 0;
    padding: 0;
    width: 1200px;
    height: 1200px;
    overflow: hidden;
  }
  .cover {
    position: relative;
    width: 1200px;
    height: 1200px;
    background: var(--sun-yellow);
    overflow: hidden;
    font-family: "Amatic SC", "Arial Narrow", sans-serif;
    color: var(--brick-red);
  }
  .paw-pattern {
    position: absolute;
    inset: 0;
    background:
      radial-gradient(ellipse at 88% 18%, rgba(253,231,102,0.55), transparent 45%),
      radial-gradient(ellipse at 35% 78%, rgba(253,231,102,0.5), transparent 45%);
  }
  .title-line {
    position: absolute;
    margin: 0;
    line-height: 1;
    white-space: nowrap;
    text-transform: uppercase;
  }
  .title-main {
    font-weight: 700;
    font-size: 218px;
    letter-spacing: 2px;
  }
  .title-main.first { left: 42px; top: 8px; }
  .title-main.second { left: 34px; top: 206px; letter-spacing: 0; }
  .title-sub {
    font-weight: 700;
    font-size: 128px;
    letter-spacing: 1px;
  }
  .title-sub.first { left: 44px; top: 420px; }
  .title-sub.second { left: 44px; top: 548px; }
  .headshot {
    position: absolute;
    left: 720px;
    top: 535px;
    width: 480px;
    height: 665px;
    border-radius: 240px 240px 0 0;
    background: linear-gradient(180deg, var(--portrait-dark) 0%, var(--portrait-tone) 22%, var(--portrait-tone) 78%, var(--portrait-dark) 100%);
  }
  .signature {
    position: absolute;
    left: 52px;
    top: 970px;
    width: 710px;
    height: 170px;
    border-radius: 85px;
    background: linear-gradient(90deg, rgba(17,17,17,0.18), rgba(17,17,17,0.08));
  }
</style>
</head>
<body>
  <main class="cover">
    <div class="paw-pattern" role="img" aria-label="Faint scattered paw print pattern"></div>
    <h1>
      <span class="title-line title-main first">Veterinary</span>
      <span class="title-line title-main second">Entrepreneurship</span>
    </h1>
    <h2>
      <span class="title-line title-sub first">The Dorian Kelboe</span>
      <span class="title-line title-sub second">Journals</span>
    </h2>
    <div class="headshot" role="img" aria-label="Head shot photo of host Dorian Kelboe"></div>
    <div class="signature" role="img" aria-label="Handwritten signature of Dorian"></div>
  </main>
</body>
</html>
```